Travel Consultant Business Card

Hello.. New travel consultant looking seeking a business card that incorporates my new logo. I specialize in cruises but also want to imply land vacation. I am very open to any design and font concepts. I'm looking for a very upbeat modern design that reflects cruise and land vacations. Bright vibrant colors

Target Market(s)

Cruise and Land Vacationers

Industry/Entity Type

Travel Agent

Contact Information for Business Card

I am very open to any design and font concepts. I'm looking for a very upbeat modern design that reflects cruise and land vacations. Bright vibrant colors

Colors

Designer to choose colors to be used in the design.

Requirements
Must have
• Company Name: MapleRidge Journeys---New logo uploaded to be included in design
• My Name: Dolores Kwiatek-Travel Consultant
• Phone Number: (555) 418-7093
• E-Mail Address: mapleridgejourneys@examplemail.net
• Website: www.mapleridgejourneys.example
Nice to have
• My tag line is …..Here to Get You There

```html
<!DOCTYPE html>
<html lang="en">
<head>
<meta charset="utf-8">
<title>MapleRidge Journeys – Business Card</title>
<link rel="stylesheet" href="https://fonts.googleapis.com/css2?family=Montserrat:wght@300;500;700&family=Quicksand:wght@400;500;700&display=swap">
<style>
  :root {
    --backdrop: #e6e8e8;
    --card-white: #ffffff;
    --card-mint: #f2f8f5;
    --brand-blue: #1d5aa6;
    --ink-navy: #1e2c44;
    --ink-dark: #2b2b2b;
    --accent-green: #1bb38a;
    --deep-teal: #0f4a43;
    --photo-wood-a: #6b4a30;
    --photo-wood-b: #a98a6c;
    --photo-map-a: #c9d6d9;
    --photo-map-b: #8fa7ad;
  }
  * { margin: 0; padding: 0; box-sizing: border-box; }
  html, body {
    width: 1200px; height: 800px; overflow: hidden;
    background: var(--backdrop);
  }
  .sheet {
    width: 1200px; height: 800px;
    display: flex; align-items: center; justify-content: center; gap: 60px;
  }
  .card {
    width: 520px; height: 297px; display: block;
    box-shadow: 0 10px 28px rgba(0,0,0,0.18);
  }
  .brand-name { font-family: "Montserrat", sans-serif; font-weight: 700; font-size: 27px; fill: var(--brand-blue); }
  .tagline { font-family: "Quicksand", sans-serif; font-weight: 500; font-size: 20px; fill: var(--ink-navy); }
  .person-first { font-family: "Montserrat", sans-serif; font-weight: 700; font-size: 21px; fill: var(--ink-dark); }
  .person-last { font-family: "Montserrat", sans-serif; font-weight: 300; font-size: 21px; fill: var(--ink-dark); }
  .person-role { font-family: "Quicksand", sans-serif; font-weight: 700; font-size: 15px; fill: var(--accent-green); }
  .contact-line { font-family: "Quicksand", sans-serif; font-weight: 500; font-size: 12.5px; fill: var(--ink-dark); }
</style>
</head>
<body>
<main class="sheet">

  <!-- Front of card -->
  <svg class="card card--front" viewBox="0 0 520 297" xmlns="http://www.w3.org/2000/svg">
    <defs>
      <linearGradient id="front-photo-tone" x1="0" y1="0" x2="1" y2="1">
        <stop offset="0" stop-color="var(--photo-wood-a)"/>
        <stop offset="0.55" stop-color="var(--photo-wood-b)"/>
        <stop offset="1" stop-color="var(--photo-map-a)"/>
      </linearGradient>
    </defs>
    <rect class="front-photo" width="520" height="297" fill="url(#front-photo-tone)"
          role="img" aria-label="Photo of a wooden desk with a laptop, a plant, a road map and a camera"/>
    <polygon class="front-panel" points="150,0 330,0 520,205 300,297 110,297 60,255" fill="var(--card-white)"/>
    <polygon class="front-corner" points="230,297 300,270 360,297" fill="var(--deep-teal)"/>
    <g class="brand-lockup">
      <circle cx="118" cy="128" r="9" fill="var(--brand-blue)"/>
      <text class="brand-name" x="136" y="138">MapleRidge Journeys</text>
    </g>
    <text class="tagline" x="150" y="185">Here to get you there</text>
  </svg>

  <!-- Back of card -->
  <svg class="card card--back" viewBox="0 0 520 297" xmlns="http://www.w3.org/2000/svg">
    <defs>
      <linearGradient id="back-photo-tone" x1="0" y1="0" x2="1" y2="1">
        <stop offset="0" stop-color="var(--photo-wood-a)"/>
        <stop offset="0.3" stop-color="var(--photo-map-a)"/>
        <stop offset="1" stop-color="var(--photo-map-b)"/>
      </linearGradient>
    </defs>
    <rect class="back-photo" width="520" height="297" fill="url(#back-photo-tone)"
          role="img" aria-label="Photo of hands holding a coffee cup and a pen over a road map"/>
    <polygon class="back-panel" points="120,0 520,0 520,250 330,297 0,150" fill="var(--card-mint)"/>
    <polygon class="back-corner" points="250,297 330,272 420,297" fill="var(--deep-teal)"/>

    <g class="person">
      <text x="480" y="62" text-anchor="end"><tspan class="person-first">DOLORES </tspan><tspan class="person-last">KWIATEK</tspan></text>
      <text class="person-role" x="480" y="84" text-anchor="end">Travel Consultant</text>
    </g>

    <g class="contacts">
      <text class="contact-line" x="446" y="177" text-anchor="end">(555) 418-7093</text>
      <text class="contact-line" x="446" y="205" text-anchor="end">mapleridgejourneys@examplemail.net</text>
      <text class="contact-line" x="446" y="233" text-anchor="end">www.mapleridgejourneys.example</text>

      <g class="icon icon--phone">
        <rect x="456" y="159" width="24" height="24" fill="var(--accent-green)"/>
        <path d="M463 165 l3 0 l1.5 3.5 l-2 1.2 a8 8 0 0 0 4 4 l1.2 -2 l3.5 1.5 l0 3 a2 2 0 0 1 -2 1.5 a13 13 0 0 1 -11 -11 a2 2 0 0 1 1.8 -1.7z" fill="#fff"/>
      </g>
      <g class="icon icon--mail">
        <rect x="456" y="187" width="24" height="24" fill="var(--accent-green)"/>
        <rect x="461" y="194" width="14" height="10" fill="none" stroke="#fff" stroke-width="1.5"/>
        <polyline points="461,194 468,200 475,194" fill="none" stroke="#fff" stroke-width="1.5"/>
      </g>
      <g class="icon icon--web">
        <rect x="456" y="215" width="24" height="24" fill="var(--accent-green)"/>
        <g fill="none" stroke="#fff" stroke-width="1.3">
          <circle cx="468" cy="227" r="7"/>
          <ellipse cx="468" cy="227" rx="3" ry="7"/>
          <line x1="461" y1="227" x2="475" y2="227"/>
        </g>
      </g>
    </g>
  </svg>

</main>
</body>
</html>
```